BrimFalcon Business Cards

We have a defined brand. Please visit our website to get a feel for the product and the color pallets. www.brimfalcon-demo.com

We need an updated, world class business card design. (See the attached existing card design). Please utilize BOTH sides of the card as shown and be creative with the layout. I do want the horse head icon to be positioned as it is with the existing card.

The remainder of the layout can be customized and I also want it vertically oriented.

Attached are the logo files and please use the colors as follows:
Green - #A5CE39
Tan - #CDBD99
Black

Feel free to play with the colors.

```html
<!DOCTYPE html>
<html lang="en">
<head>
<meta charset="utf-8">
<title>BrimFalcon Labs – Business Card</title>
<link rel="stylesheet" href="https://fonts.googleapis.com/css2?family=Open+Sans:wght@400;600;700&display=swap">
<style>
  :root {
    --green: #a5ce39;
    --black: #111111;
    --white: #ffffff;
    --stage: #e9e6df;
    --text: #1a1a1a;
  }
  * { box-sizing: border-box; margin: 0; padding: 0; }
  html, body {
    width: 1200px; height: 900px; overflow: hidden;
    background: var(--stage);
    font-family: "Open Sans", Arial, sans-serif;
    color: var(--text);
  }
  .stage {
    position: relative; width: 1200px; height: 900px;
    display: flex; justify-content: center; align-items: center; gap: 120px;
  }
  .card {
    position: relative; width: 350px; height: 610px;
    background: var(--white);
    border: 6px solid var(--green);
    border-radius: 26px;
    box-shadow: 0 10px 26px rgba(0,0,0,.18);
  }

  /* Front */
  .card-front { padding: 30px 26px 34px; display: flex; flex-direction: column; }
  .brand { display: flex; align-items: center; gap: 10px; margin-bottom: 22px; }
  .brand-dot { width: 40px; height: 40px; border-radius: 50%; background: var(--black); flex: none; }
  .brand-text { display: flex; flex-direction: column; line-height: 1; }
  .brand-name { font-weight: 700; font-size: 30px; color: var(--black); letter-spacing: -.5px; }
  .brand-tagline { font-size: 12px; letter-spacing: 3px; margin-top: 5px; color: var(--black); }

  .info-list { list-style: none; display: flex; flex-direction: column; gap: 14px; flex: 1; }
  .info-pill {
    flex: 1;
    display: flex; align-items: center; gap: 14px;
    background: var(--green);
    border: 3px solid var(--black);
    border-radius: 16px;
    padding: 0 16px;
    font-size: 16px;
  }
  .info-pill.name-pill { flex-direction: column; justify-content: center; gap: 0; text-align: center; flex: 1.15; }
  .person-name { font-weight: 700; font-size: 22px; }
  .person-role { font-size: 16px; }
  .info-icon { width: 24px; height: 24px; flex: none; fill: var(--black); }
  .info-text { line-height: 1.25; word-break: break-word; }

  /* Back */
  .card-back { display: flex; flex-direction: column; align-items: center; }
  .mark {
    margin-top: 70px;
    display: flex; flex-direction: column; align-items: center; gap: 22px;
  }
  .mark-circle { width: 230px; height: 230px; border-radius: 50%; background: var(--black); }
  .mark-name { font-weight: 700; font-size: 34px; color: var(--black); }
  .tm { position: absolute; top: 72px; right: 44px; font-size: 12px; }
  .site {
    position: absolute; bottom: 34px; left: 0; right: 0; text-align: center;
    font-size: 19px; letter-spacing: .3px;
  }
  .site .accent { color: var(--green); }
</style>
</head>
<body>
<main class="stage">

  <section class="card card-front" aria-label="Business card front">
    <header class="brand">
      <span class="brand-dot"></span>
      <div class="brand-text">
        <span class="brand-name">BrimFalcon Labs</span>
        <span class="brand-tagline">Performance Driven EVs</span>
      </div>
    </header>

    <ul class="info-list">
      <li class="info-pill name-pill">
        <span class="person-name">Darren Kolt</span>
        <span class="person-role">President &amp; CEO</span>
      </li>
      <li class="info-pill">
        <svg class="info-icon" viewBox="0 0 24 24" aria-hidden="true"><path d="M3 9c0-2 3-4 9-4s9 2 9 4v2h-4V9.5c-1-.6-3-1-5-1s-4 .4-5 1V11H3z"/><path d="M6 12h12l2 7H4z"/></svg>
        <span class="info-text">306.555.0147</span>
      </li>
      <li class="info-pill">
        <svg class="info-icon" viewBox="0 0 24 24" aria-hidden="true"><path d="M2 5h20v14H2z M3.5 6.5 12 13l8.5-6.5" fill="var(--black)"/><path d="M4 7l8 6 8-6" fill="none" stroke="var(--green)" stroke-width="1.5"/></svg>
        <span class="info-text">darren@brimfalcon-demo.com</span>
      </li>
      <li class="info-pill">
        <svg class="info-icon" viewBox="0 0 24 24" aria-hidden="true"><circle cx="12" cy="12" r="10"/><path d="M2 12h20M12 2c3 3 3 17 0 20M12 2c-3 3-3 17 0 20" fill="none" stroke="var(--green)" stroke-width="1.4"/></svg>
        <span class="info-text">www.brimfalconlabs-demo.com</span>
      </li>
      <li class="info-pill">
        <svg class="info-icon" viewBox="0 0 24 24" aria-hidden="true"><path d="M12 1a7 7 0 0 0-7 7c0 5 7 15 7 15s7-10 7-15a7 7 0 0 0-7-7zm0 10a3 3 0 1 1 0-6 3 3 0 0 1 0 6z"/></svg>
        <span class="info-text">Aldenridge, Westmark<br>canada</span>
      </li>
    </ul>
  </section>

  <section class="card card-back" aria-label="Business card back">
    <div class="mark">
      <span class="mark-circle"></span>
      <span class="mark-name">BrimFalcon</span>
    </div>
    <span class="tm">TM</span>
    <p class="site">www.<span class="accent">BrimFalconLabs</span>-demo.com</p>
  </section>

</main>
</body>
</html>
```